Varro's Electrical & Solar Corflute Signage Design

So my plan is to put this design onto a 600 by 400 corflute sign (this sign will be printed out and cable tied to a fence FYI). I would like to have the name and the icon stand out. I need Varro's Electrical & Solar to be big and clear and I would like to have my "S" icon faded behind "Varro's Electrical & Solar" in the background.

I want to have my Lic No. - Top left with my ABN directly underneath. (I Want two ticks infront of them like this)
✓ Lic No. 582164K
✓ ABN 41 276 519 683

I want to have written on it: ALL ASPECTS OF ELECTRICAL (please use cool fonts and nothing too plain)
I also want to have: YOUR LOCAL TRUSTED ELECTRICIAN but if it looks too dicky then just have "all aspects of electrical" and just "free quotes • fast service" somewhere.
Directly underneath (smaller but still clear): FREE QUOTES • FAST SERVICE

At the bottom, I need my phone number big and clear - 0438 617 905 I would like this on a banner meaning like a cool strip at the bottom. (Please make the strip/banner look cool and not boring. Maybe shade the colour or something)
I also want the Facebook & Instagram icons on there so people can look us up on facebook & Instagram (make them match the colour of my logo or you could try any other colour that works)
Thank you so much!!

Colors

Designer to choose colors to be used in the design.

Requirements
Should not have
• no different colours other then the colours on my logo and icon

```html
<!DOCTYPE html>
<html lang="en">
<head>
<meta charset="utf-8">
<title>Varro's Electrical &amp; Solar – Corflute Sign</title>
<link rel="stylesheet" href="https://fonts.googleapis.com/css2?family=Anton&family=Archivo:wght@800&family=Lato:wght@900&family=Open+Sans:wght@700&display=swap">
<style>
  :root {
    --page-grey: #c2c2c2;
    --sign-black: #151515;
    --band-dark: #1d1d1d;
    --band-mid: #232323;
    --green-deep: #1cb833;
    --green-bright: #3fdf57;
    --green-text: #22c03a;
    --silver-light: #e4e6e9;
    --silver-dark: #9aa0a7;
    --quote-grey: #9fa4aa;
    --ink: #050505;
    --white: #ffffff;
  }
  html, body {
    margin: 0;
    width: 1200px;
    height: 848px;
    overflow: hidden;
    background: var(--page-grey);
  }
  .sign {
    position: absolute;
    left: 206px;
    top: 161px;
    width: 788px;
    height: 525px;
    display: block;
  }
  .credential { font-family: "Lato", sans-serif; font-weight: 900; font-size: 20px; }
  .credential-label { fill: var(--green-text); }
  .credential-value { fill: var(--white); }
  .tick { fill: none; stroke: var(--green-text); stroke-width: 4; stroke-linecap: square; }
  .brand-name { font-family: "Anton", sans-serif; fill: var(--green-text); }
  .tagline { font-family: "Anton", sans-serif; font-size: 62px; fill: url(#greenFace); }
  .services { font-family: "Open Sans", sans-serif; font-weight: 700; font-size: 24px; fill: var(--quote-grey); letter-spacing: 2px; }
  .services-dot { fill: var(--green-text); }
  .phone { font-family: "Archivo", sans-serif; font-weight: 800; font-size: 84px; fill: var(--ink); }
  .social-ring { fill: none; stroke: var(--quote-grey); stroke-width: 1.6; }
  .social-core { fill: none; stroke: var(--green-text); stroke-width: 2.5; }
</style>
</head>
<body>
<svg class="sign" viewBox="0 0 788 525" xmlns="http://www.w3.org/2000/svg" role="img" aria-label="Varro's Electrical and Solar sign">
  <defs>
    <linearGradient id="greenFace" x1="0" y1="0" x2="0" y2="1">
      <stop offset="0" stop-color="var(--green-deep)"/>
      <stop offset="0.55" stop-color="var(--green-bright)"/>
      <stop offset="1" stop-color="var(--green-deep)"/>
    </linearGradient>
    <linearGradient id="bannerFace" x1="0" y1="0" x2="0" y2="1">
      <stop offset="0" stop-color="var(--green-deep)"/>
      <stop offset="0.45" stop-color="var(--green-bright)"/>
      <stop offset="1" stop-color="var(--green-deep)"/>
    </linearGradient>
    <linearGradient id="silverFace" x1="0" y1="0" x2="0" y2="1">
      <stop offset="0" stop-color="var(--silver-dark)"/>
      <stop offset="0.6" stop-color="var(--silver-light)"/>
      <stop offset="1" stop-color="var(--silver-dark)"/>
    </linearGradient>
  </defs>

  <!-- sign board -->
  <rect class="board" width="788" height="525" fill="var(--sign-black)"/>

  <!-- background diagonal bands -->
  <g class="background-bands">
    <polygon points="300,525 420,380 520,300 788,180 788,330 620,525" fill="var(--band-dark)"/>
    <polygon points="510,525 600,360 788,255 788,290 640,420 560,525" fill="var(--band-mid)"/>
    <polygon points="575,525 680,390 788,345 788,525" fill="var(--band-mid)"/>
  </g>

  <!-- licence and ABN -->
  <g class="credentials">
    <polyline class="tick" points="36,39 42,45 52,35"/>
    <text class="credential" x="58" y="46"><tspan class="credential-label">Lic No.</tspan> <tspan class="credential-value">582164K</tspan></text>
    <polyline class="tick" points="35,64 41,70 51,60"/>
    <text class="credential" x="57" y="70"><tspan class="credential-label">ABN</tspan> <tspan class="credential-value">41 276 519 683</tspan></text>
  </g>

  <!-- business name -->
  <g class="brand">
    <text class="brand-name" x="394" y="190" font-size="112" text-anchor="middle" textLength="560" lengthAdjust="spacingAndGlyphs">VARRO'S</text>
    <text class="brand-name" x="394" y="218" font-size="24" text-anchor="middle" textLength="540" lengthAdjust="spacing">ELECTRICAL &amp; SOLAR</text>
  </g>

  <!-- headline -->
  <text class="tagline" x="40" y="299" textLength="708" lengthAdjust="spacingAndGlyphs">ALL ASPECTS OF ELECTRICAL</text>

  <!-- services line -->
  <text class="services" x="197" y="339" textLength="373" lengthAdjust="spacing">FREE QUOTES <tspan class="services-dot">•</tspan> FAST SERVICE</text>

  <!-- phone banner -->
  <g class="phone-banner">
    <polygon class="banner-wing" points="0,356 54,356 0,431" fill="url(#silverFace)"/>
    <polygon class="banner-wing" points="734,356 788,356 788,429" fill="url(#silverFace)"/>
    <polygon class="banner-strip" points="75,356 712,356 788,457 0,457" fill="url(#bannerFace)"/>
    <text class="phone" x="89" y="439" textLength="601" lengthAdjust="spacingAndGlyphs">0438 617 905</text>
  </g>

  <!-- social links -->
  <g class="social-links" aria-label="Social media links">
    <circle class="social-ring" cx="691" cy="494" r="18"/>
    <circle class="social-core" cx="691" cy="494" r="8"/>
    <circle class="social-ring" cx="732" cy="494" r="18"/>
    <circle class="social-core" cx="732" cy="494" r="8"/>
  </g>
</svg>
</body>
</html>
```